Simple, elegant, business card design required

Hi designers,I am looking for a simple yet elegant business card design.

Please make use of my logo (attached); you are free to tweak the logo should you wish to do so.

Our business is involved in many different fields - almost all of them involved in some form of "design", so that's really one of the key things I want to portray. I do not wish to specify which field of design, exactly.

I prefer white on black (or just monochromatic), but if you have a different, creative idea, I am open to that too.

You can use artsy photographs provided that you have the license to use those. Please feel free to ask me any questions.
Updates

Project Deadline Extended Reason: Small extension for potential revisions. Did not get the time to provide as much feedback as I can. Added Wednesday, July 09, 2014

Target Market(s)

High-end customers looking for design consultancy

Industry/Entity Type

Business

Contact Information for Business Card

Name: Gareth Moonfield
Position: Creative Director
Mobile: +155603928174
Address: Barrow Lane, Ashcombe on Wey, Dunmorshire GL12 4RT
Website: torvakest.com (not launched yet)

Requirements
Must have
• Design layout must be clean, original, and text must be readable when printed.
Should not have
• ~ No business card templates please. Anyone using this will be reported.
• ~ Please don't spam entries.

```html
<!DOCTYPE html>
<html lang="en">
<head>
<meta charset="utf-8">
<title>Torvakest Business Card</title>
<link href="https://fonts.googleapis.com/css2?family=Open+Sans:wght@400&family=Roboto+Condensed:wght@400&display=swap" rel="stylesheet">
<style>
  :root {
    --backdrop: #3b3b3b;
    --ink: #231f20;
    --paper: #ffffff;
    --text-dark: #1e1b1c;
    --icon-muted: #777777;
  }
  * { margin: 0; padding: 0; box-sizing: border-box; }
  html, body {
    width: 1200px;
    height: 750px;
    overflow: hidden;
    background: var(--backdrop);
  }
  .stage {
    position: relative;
    width: 1200px;
    height: 750px;
  }
  .card {
    position: absolute;
    top: 210px;
    width: 514px;
    height: 294px;
    overflow: hidden;
  }
  .card--back { left: 75px; background: var(--ink); }
  .card--front { left: 609px; background: var(--paper); }

  .brand-block {
    position: absolute;
    width: 144px;
    height: 84px;
  }
  .card--back .brand-block { left: 191px; top: 186px; background: var(--paper); }
  .card--front .brand-block { left: 25px; top: 23px; background: var(--ink); }

  .brand-name {
    position: absolute;
    font-family: "Roboto Condensed", sans-serif;
    font-weight: 400;
    font-size: 23px;
    letter-spacing: 4.6px;
    line-height: 1;
  }
  .card--back .brand-name { left: 349px; top: 217px; color: var(--paper); }
  .card--front .brand-name { left: 183px; top: 54px; color: var(--ink); }

  .holder {
    position: absolute;
    right: 25px;
    top: 140px;
    text-align: right;
    font-family: "Open Sans", sans-serif;
    color: var(--text-dark);
  }
  .holder-name { font-size: 18.5px; letter-spacing: -0.6px; line-height: 1.1; }
  .holder-role { font-size: 13.5px; letter-spacing: -0.2px; line-height: 1.3; }

  .edge-tab {
    position: absolute;
    right: 0;
    top: 146px;
    width: 17px;
    height: 28px;
    background: var(--ink);
  }

  .contacts {
    position: absolute;
    right: 29px;
    top: 196px;
    list-style: none;
    font-family: "Open Sans", sans-serif;
    font-size: 13.5px;
    color: var(--text-dark);
    letter-spacing: -0.1px;
  }
  .contact {
    display: flex;
    justify-content: flex-end;
    align-items: flex-start;
    line-height: 20px;
  }
  .contact-text { text-align: right; }
  .contact-icon {
    flex: none;
    width: 10px;
    height: 12px;
    margin: 4px 0 0 8px;
  }
</style>
</head>
<body>
<main class="stage">
  <section class="card card--back" aria-label="Card back">
    <div class="brand-block"></div>
    <span class="brand-name">TORVAKEST</span>
  </section>

  <section class="card card--front" aria-label="Card front">
    <div class="brand-block"></div>
    <span class="brand-name">TORVAKEST</span>

    <div class="holder">
      <p class="holder-name">Gareth Moonfield Position</p>
      <p class="holder-role">Creative Director</p>
    </div>
    <div class="edge-tab"></div>

    <ul class="contacts">
      <li class="contact">
        <span class="contact-text">+155603928174</span>
        <svg class="contact-icon" viewBox="0 0 10 12" aria-hidden="true">
          <rect x="2" y="1" width="6" height="10" rx="1.2" fill="none" stroke="var(--text-dark)" stroke-width="1.6"/>
        </svg>
      </li>
      <li class="contact">
        <span class="contact-text">torvakest.com</span>
        <svg class="contact-icon" viewBox="0 0 10 12" aria-hidden="true">
          <g fill="none" stroke="var(--icon-muted)" stroke-width="0.8">
            <circle cx="5" cy="6" r="4"/>
            <ellipse cx="5" cy="6" rx="1.8" ry="4"/>
            <line x1="1" y1="6" x2="9" y2="6"/>
          </g>
        </svg>
      </li>
      <li class="contact">
        <span class="contact-text">Barrow Lane, Ashcombe on Wey<br>Dunmorshire GL12 4RT</span>
        <svg class="contact-icon" viewBox="0 0 10 12" aria-hidden="true">
          <path d="M5 11 C3 8 2 6.5 2 4.8 A3 3 0 0 1 8 4.8 C8 6.5 7 8 5 11 Z" fill="var(--text-dark)"/>
          <circle cx="5" cy="4.8" r="1.1" fill="var(--paper)"/>
        </svg>
      </li>
    </ul>
  </section>
</main>
</body>
</html>
```